Business card design needed

I am branching out into the world of private practice in Speech Pathology. My clients will be aged 0-17; the business card will be distributed within my existing teacher and parent networks in schools.

I work with clients to develop their speech, language, literacy, fluency, swallowing and voice. I like to think that parents hand over their money to me because I've offered a fun session with positive outcomes/growth and for an affordable price.

I'm flexible with colours; though think something bright would be ideal. I'm not wanting anything too cutesy or 'little kid'. I'd like for it to stand out in a bulging purse or on a fridge crammed with papers.

Industry/Entity Type

Teacher

Contact Information for Business Card

Wren Bloom Speech Pathology Pty Ltd
Kate Hollister
Speech Pathologist
Ph: 0418 962 307
Email: katehollister@mailvane.com

Logo Text

Logo styles of interest
Character Logo
Wordmark Logo
Lettermark Logo
Requirements
Must have
• A kind of graphic to represent the core business - that is, providing intervention to children 0-17 with communication needs (e.g., speech, language, literacy, swallowing, voice, fluency)

Should not have
• Pictures of babies or children.
Love hearts.

```html
<!DOCTYPE html>
<html lang="en">
<head>
<meta charset="utf-8">
<title>Wren Bloom Speech Pathology – Business Card</title>
<link rel="stylesheet" href="https://fonts.googleapis.com/css2?family=Quicksand:wght@500;600;700&family=Open+Sans:wght@700&display=swap">
<style>
  :root {
    --stage: #e9ecef;
    --card-blue: #1c9fe6;
    --card-blue-deep: #138ad3;
    --facet-light: rgba(255, 255, 255, 0.16);
    --facet-soft: rgba(255, 255, 255, 0.09);
    --ink: #0b2238;
    --rule: #ffffff;
  }
  * { margin: 0; padding: 0; box-sizing: border-box; }
  html, body {
    width: 1200px;
    height: 849px;
    overflow: hidden;
    background: var(--stage);
  }
  .canvas {
    position: relative;
    width: 1200px;
    height: 849px;
  }
  .card {
    position: absolute;
    left: 380px;
    top: 52px;
    width: 440px;
    height: 745px;
    border-radius: 28px;
    overflow: hidden;
    background: linear-gradient(160deg, var(--card-blue) 0%, var(--card-blue-deep) 100%);
    box-shadow: 0 10px 30px rgba(0, 0, 0, 0.18);
    color: var(--ink);
    font-family: 'Quicksand', sans-serif;
  }
  .card__facets {
    position: absolute;
    inset: 0;
  }
  .brand {
    position: absolute;
    left: 40px;
    top: 70px;
    right: 40px;
    display: flex;
    align-items: center;
    gap: 18px;
  }
  .brand__dot {
    flex: none;
    width: 46px;
    height: 46px;
    border-radius: 50%;
    background: var(--ink);
  }
  .brand__name {
    font-family: 'Quicksand', sans-serif;
    font-weight: 700;
    font-size: 30px;
    line-height: 1.15;
    color: var(--ink);
  }
  .identity {
    position: absolute;
    top: 318px;
    left: 0;
    right: 0;
    text-align: center;
  }
  .identity__name {
    font-weight: 600;
    font-size: 38px;
    letter-spacing: 0.5px;
  }
  .identity__rule {
    width: 250px;
    height: 3px;
    margin: 8px auto 10px;
    background: var(--rule);
  }
  .identity__title {
    font-family: 'Open Sans', sans-serif;
    font-weight: 700;
    font-size: 19px;
  }
  .contact {
    position: absolute;
    top: 460px;
    left: 78px;
    list-style: none;
  }
  .contact__item {
    display: flex;
    align-items: center;
    gap: 18px;
    font-weight: 600;
    font-size: 20px;
    margin-bottom: 16px;
  }
  .contact__icon {
    width: 20px;
    height: 20px;
    flex: none;
  }
  .mission {
    position: absolute;
    left: 34px;
    right: 34px;
    bottom: 46px;
    font-family: 'Quicksand', sans-serif;
    font-weight: 700;
    font-size: 15px;
    line-height: 1.45;
  }
  .mission__mark {
    font-family: 'Open Sans', sans-serif;
    font-size: 30px;
    line-height: 0;
    vertical-align: -10px;
  }
  .mission__mark--close {
    display: block;
    text-align: right;
    margin-top: 18px;
  }
</style>
</head>
<body>
<main class="canvas">
  <article class="card">
    <svg class="card__facets" viewBox="0 0 440 745" aria-hidden="true">
      <polygon points="0,0 300,0 0,260" fill="var(--facet-soft)"/>
      <polygon points="440,120 440,520 120,745 60,745" fill="var(--facet-light)"/>
      <polygon points="0,430 260,745 0,745" fill="var(--facet-soft)"/>
      <polygon points="440,0 440,300 250,0" fill="var(--facet-soft)"/>
    </svg>

    <header class="brand">
      <span class="brand__dot"></span>
      <h1 class="brand__name">Wren Bloom Speech Pathology Pty Ltd</h1>
    </header>

    <section class="identity">
      <h2 class="identity__name">Kate Hollister</h2>
      <div class="identity__rule"></div>
      <p class="identity__title">Speech Pathologist</p>
    </section>

    <ul class="contact">
      <li class="contact__item">
        <svg class="contact__icon" viewBox="0 0 24 24" aria-hidden="true">
          <path fill="var(--ink)" d="M6.6 10.8a15.1 15.1 0 0 0 6.6 6.6l2.2-2.2a1 1 0 0 1 1-.25 11.4 11.4 0 0 0 3.6.57 1 1 0 0 1 1 1V20a1 1 0 0 1-1 1A17 17 0 0 1 3 4a1 1 0 0 1 1-1h3.5a1 1 0 0 1 1 1c0 1.25.2 2.45.57 3.57a1 1 0 0 1-.25 1z"/>
        </svg>
        <span>0418 962 307</span>
      </li>
      <li class="contact__item">
        <svg class="contact__icon" viewBox="0 0 24 24" aria-hidden="true">
          <rect x="2" y="5" width="20" height="14" rx="2" fill="var(--ink)"/>
          <path d="M3 6.5l9 6.5 9-6.5" fill="none" stroke="var(--card-blue)" stroke-width="1.8"/>
        </svg>
        <span>katehollister@mailvane.com</span>
      </li>
    </ul>

    <p class="mission">
      <span class="mission__mark">&ldquo;</span> Providing fun, effective and affordable intervention to support development of speech and language skills in children and adolescents.
      <span class="mission__mark mission__mark--close">&rdquo;</span>
    </p>
  </article>
</main>
</body>
</html>
```